New Business Card for Casual Beachfront Cafe

Quirky Beachfront Cafe at Moana, South Australia needs a DOUBLE SIDED business card to print on PrintHollow.

Target Market(s)

Business Cards sit on the counter for Guests to take with them. Please view our website www.saltkettlecafe.com.au to get a feel for the Cafe. You may also view our Instagram at @saltkettlecafe

Industry/Entity Type

Cafe / Restaurant

Contact Information for Business Card

Information equivalent to: Breakfast, Lunch, Dinner, Coffee, Takeaway / 918 Marlin Road Saltreef Bay 5999 / Menu & Opening Hours: www.saltkettlecafe.com.au / ph (08) 7194 2618

Requirements
Must have
• Information equivalent to: Breakfast, Lunch, Dinner, Coffee, Takeaway / 918 Marlin Road Saltreef Bay 5999 / Menu & Opening Hours: www.saltkettlecafe.com.au / ph (08) 7194 2618
Nice to have
• Potentially some of our trademark colours (Cafe can be searched via Google)
Should not have
• Must NOT have image of the building. May have the logo provided on one side but not necessarily, depending on how you wish to design the card

```html
<!DOCTYPE html>
<html lang="en">
<head>
<meta charset="utf-8">
<title>Salt Kettle Cafe – Business Card</title>
<link rel="stylesheet" href="https://fonts.googleapis.com/css2?family=Montserrat:wght@500;600;900&display=swap">
<style>
  :root {
    --navy: #11457e;
    --white: #ffffff;
    --yellow: #f9f200;
    --orange: #f7a93b;
    --coral: #f7745a;
    --teal: #0fb894;
    --stage: #3b3b3b;
    --divider: rgba(255,255,255,0.45);
  }
  * { box-sizing: border-box; margin: 0; padding: 0; }
  html, body { width: 1200px; height: 1200px; overflow: hidden; }
  body {
    background: var(--stage);
    font-family: "Montserrat", sans-serif;
    display: flex;
    flex-direction: column;
    align-items: center;
    justify-content: center;
    gap: 70px;
  }
  .card {
    position: relative;
    width: 860px;
    height: 491px;
    border-radius: 38px;
    overflow: hidden;
    box-shadow: 0 18px 40px rgba(0,0,0,0.35);
  }

  /* Front */
  .card--front { background: var(--white); }
  .front__name {
    position: absolute; top: 0; left: 0; right: 0; height: 238px;
    display: flex; align-items: center; justify-content: center;
    text-align: center;
    color: var(--navy);
    font-weight: 900;
    font-size: 62px;
    line-height: 1.02;
    letter-spacing: 1px;
    text-transform: uppercase;
  }
  .front__lower {
    position: absolute; left: 0; right: 0; bottom: 0; top: 250px;
    background: var(--navy);
  }
  .accent-stripe {
    position: absolute; left: 0; right: 0; top: 238px; height: 12px;
    display: flex;
  }
  .accent-stripe span { display: block; height: 100%; }
  .accent-stripe .teal-a { width: 33%; background: var(--teal); }
  .accent-stripe .orange { width: 19%; background: var(--orange); }
  .accent-stripe .coral { width: 19%; background: var(--coral); }
  .accent-stripe .teal-b { flex: 1; background: var(--teal); }

  .contact {
    position: absolute; left: 92px; top: 296px;
    color: var(--white);
  }
  .contact__heading {
    color: var(--orange);
    font-weight: 600;
    font-size: 19px;
    letter-spacing: 0.5px;
    margin-bottom: 12px;
  }
  .contact__row {
    display: flex; align-items: center; gap: 12px;
    font-weight: 500; font-size: 20px;
    margin-bottom: 10px;
    white-space: nowrap;
  }
  .contact__row svg { width: 22px; height: 22px; flex: none; }

  .front__divider {
    position: absolute; left: 520px; top: 290px; width: 1px; height: 150px;
    background: var(--divider);
  }

  .services {
    position: absolute; left: 580px; top: 296px;
    list-style: none;
    color: var(--white);
    font-weight: 500; font-size: 21px;
    letter-spacing: 0.5px;
  }
  .services li { display: flex; align-items: center; gap: 12px; margin-bottom: 6px; }
  .services .bullet {
    width: 9px; height: 9px; border-radius: 50%; background: var(--orange); flex: none;
  }

  /* Back */
  .card--back {
    background: var(--navy);
    display: flex; align-items: center; justify-content: center;
  }
  .back__name {
    color: var(--yellow);
    font-weight: 900;
    font-size: 88px;
    line-height: 1.02;
    text-align: center;
    text-transform: uppercase;
    letter-spacing: 2px;
  }
</style>
</head>
<body>
  <section class="card card--front" aria-label="Card front">
    <div class="front__name">Salt Kettle<br>Cafe</div>
    <div class="front__lower"></div>
    <div class="accent-stripe"><span class="teal-a"></span><span class="orange"></span><span class="coral"></span><span class="teal-b"></span></div>

    <div class="contact">
      <p class="contact__heading">MENU &amp; OPENING HOURS:</p>
      <p class="contact__row">
        <svg viewBox="0 0 24 24" aria-hidden="true"><path fill="#f7a93b" d="M6.6 10.8a15.5 15.5 0 0 0 6.6 6.6l2.2-2.2a1 1 0 0 1 1-.25 11.4 11.4 0 0 0 3.6.57 1 1 0 0 1 1 1V20a1 1 0 0 1-1 1A17 17 0 0 1 3 4a1 1 0 0 1 1-1h3.5a1 1 0 0 1 1 1c0 1.25.2 2.45.57 3.57a1 1 0 0 1-.25 1z"/></svg>
        (08) 7194 2618
      </p>
      <p class="contact__row">
        <svg viewBox="0 0 24 24" aria-hidden="true"><g fill="none" stroke="#f7a93b" stroke-width="2"><circle cx="12" cy="12" r="9"/><ellipse cx="12" cy="12" rx="4" ry="9"/><path d="M3 12h18M5 7h14M5 17h14"/></g></svg>
        www.saltkettlecafe.com.au
      </p>
      <p class="contact__row">
        <svg viewBox="0 0 24 24" aria-hidden="true"><path fill="#f7a93b" d="M12 2a7 7 0 0 0-7 7c0 5 7 13 7 13s7-8 7-13a7 7 0 0 0-7-7zm0 9.5A2.5 2.5 0 1 1 12 6.5a2.5 2.5 0 0 1 0 5z"/></svg>
        918 Marlin Road Saltreef Bay 5999
      </p>
    </div>

    <div class="front__divider"></div>

    <ul class="services">
      <li><span class="bullet"></span>BREAKFAST</li>
      <li><span class="bullet"></span>LUNCH</li>
      <li><span class="bullet"></span>DINNER</li>
      <li><span class="bullet"></span>COFFEE</li>
      <li><span class="bullet"></span>TAKEAWAY</li>
    </ul>
  </section>

  <section class="card card--back" aria-label="Card back">
    <div class="back__name">Salt Kettle<br>Cafe</div>
  </section>
</body>
</html>
```